Clean professional business card design

Need a professional looking, high quality card and letterhead design. Business card would prefer to have a grey tone to the background.

Back of card needs to have: "Securities offered through Norvane Capital Partners LLC (doing Insurance business in CA as NKPTR Insurance Agency), member BRAXEL/TOVMA. Advisory services offered through Norvane Wealth Counsel LLC. Norvane entities are under separate ownership from any other named entity. [employee name] CA Insurance Lic #7K21904

Industry/Entity Type

Financial Planning

Font styles to use
Serif
Sans Serif

Requirements
Must have
• Customization of text so that I can adjust for other employee

```html
<!DOCTYPE html>
<html lang="en">
<head>
<meta charset="utf-8">
<title>Keystead Financial Advisers – Business Card</title>
<link rel="stylesheet" href="https://fonts.googleapis.com/css2?family=Cinzel:wght@400;700&family=Open+Sans:wght@400;600&display=swap">
<style>
  :root {
    --page-bg: #f4f5f6;
    --card-grey: #e3e5e8;
    --card-grey-dark: #4e555d;
    --brand-blue: #0a6fb8;
    --text-dark: #3a3d41;
    --on-dark: #ffffff;
    --on-dark-soft: #d9dde1;
  }
  * { box-sizing: border-box; margin: 0; padding: 0; }
  html, body {
    width: 1200px;
    height: 900px;
    overflow: hidden;
    background: var(--page-bg);
    font-family: "Open Sans", sans-serif;
  }
  .canvas { position: relative; width: 1200px; height: 900px; }

  .card {
    position: absolute;
    width: 520px;
    height: 297px;
    box-shadow: 0 10px 24px rgba(0,0,0,0.14);
  }

  /* Front */
  .card-front {
    left: 60px;
    top: 440px;
    background: var(--card-grey);
    color: var(--text-dark);
  }
  .holder { position: absolute; left: 30px; top: 28px; }
  .holder-name {
    font-family: "Cinzel", serif;
    font-weight: 700;
    font-size: 16px;
    letter-spacing: 0.5px;
    text-transform: uppercase;
    color: var(--brand-blue);
  }
  .holder-role { font-size: 11px; margin-top: 2px; }

  .contacts {
    position: absolute;
    left: 30px;
    top: 124px;
    list-style: none;
    font-size: 12px;
    line-height: 20px;
  }
  .contacts li { display: flex; align-items: center; gap: 7px; }
  .contacts svg { width: 11px; height: 11px; fill: var(--brand-blue); }

  .brand {
    display: flex;
    align-items: center;
    gap: 10px;
    font-family: "Cinzel", serif;
    font-weight: 400;
  }
  .brand-mark { width: 18px; height: 18px; background: currentColor; flex: none; }
  .brand-name { line-height: 1.05; }
  .brand-name .word { display: block; font-size: 30px; letter-spacing: 1px; }
  .brand-name .tag { display: block; font-size: 13.5px; letter-spacing: 2.8px; }
  .card-front .brand { position: absolute; right: 28px; top: 118px; color: var(--brand-blue); }

  .details {
    position: absolute;
    right: 30px;
    bottom: 26px;
    text-align: right;
    font-size: 12px;
    line-height: 17px;
  }
  .licence { color: var(--brand-blue); font-size: 13px; margin-bottom: 2px; }

  /* Back */
  .card-back {
    left: 620px;
    top: 150px;
    background: var(--card-grey-dark);
    display: flex;
    flex-direction: column;
    align-items: center;
    justify-content: center;
    gap: 22px;
    padding: 0 34px;
  }
  .card-back .brand { color: var(--on-dark); }
  .card-back .brand-name .word { font-size: 34px; }
  .card-back .brand-name .tag { font-size: 15px; letter-spacing: 3.2px; }
  .card-back .brand-mark { width: 20px; height: 20px; }

  .disclosure {
    font-size: 9.5px;
    line-height: 14px;
    color: var(--on-dark-soft);
    text-align: center;
  }
  .disclosure .employee { color: var(--on-dark); font-weight: 600; }
</style>
</head>
<body>
<main class="canvas">

  <section class="card card-front" aria-label="Business card front">
    <div class="holder">
      <p class="holder-name">Daniel Hartwell</p>
      <p class="holder-role">CA Insurance</p>
    </div>

    <ul class="contacts">
      <li>
        <svg viewBox="0 0 24 24" aria-hidden="true"><path d="M6.6 10.8a15.1 15.1 0 0 0 6.6 6.6l2.2-2.2c.3-.3.7-.4 1-.2 1.1.4 2.3.6 3.6.6.6 0 1 .4 1 1V20c0 .6-.4 1-1 1A17 17 0 0 1 3 4c0-.6.4-1 1-1h3.5c.6 0 1 .4 1 1 0 1.3.2 2.5.6 3.6.1.3 0 .7-.2 1z"/></svg>
        (044)987654321
      </li>
      <li>
        <svg viewBox="0 0 24 24" aria-hidden="true"><path d="M2 5h20v14H2zm2 2v.5l8 5 8-5V7l-8 5z"/></svg>
        info@keysteadfa.com
      </li>
      <li>
        <svg viewBox="0 0 24 24" aria-hidden="true"><path d="M12 2a10 10 0 1 0 0 20 10 10 0 0 0 0-20zm0 2c.8 1.2 1.5 2.5 1.9 4h-3.8c.4-1.5 1.1-2.8 1.9-4zM4.3 14a8 8 0 0 1 0-4h3.4a16 16 0 0 0 0 4zm5.4 0a14 14 0 0 1 0-4h4.6a14 14 0 0 1 0 4zm6.6 0a16 16 0 0 0 0-4h3.4a8 8 0 0 1 0 4zM12 20c-.8-1.2-1.5-2.5-1.9-4h3.8c-.4 1.5-1.1 2.8-1.9 4z"/></svg>
        www.keysteadfa.com
      </li>
    </ul>

    <div class="brand">
      <span class="brand-mark" aria-hidden="true"></span>
      <p class="brand-name"><span class="word">KEYSTEAD</span><span class="tag">FINANCIAL ADVISERS</span></p>
    </div>

    <div class="details">
      <p class="licence">Lic #7K21904</p>
      <p>56, Marlow Street,</p>
      <p>Fenwick, 40218</p>
    </div>
  </section>

  <section class="card card-back" aria-label="Business card back">
    <div class="brand">
      <span class="brand-mark" aria-hidden="true"></span>
      <p class="brand-name"><span class="word">KEYSTEAD</span><span class="tag">FINANCIAL ADVISERS</span></p>
    </div>
    <p class="disclosure">
      Securities offered through Norvane Capital Partners LLC (doing Insurance business in CA as NKPTR Insurance Agency), member BRAXEL/TOVMA. Advisory services offered through Norvane Wealth Counsel LLC. Norvane entities are under separate ownership from any other named entity.<br>
      <span class="employee">Daniel Hartwell</span> CA Insurance Lic #7K21904
    </p>
  </section>

</main>
</body>
</html>
```